Word Page Templates x 5

1 x Letterhead Template with Header and Footer able to be printed to paper and pdf with non blurry resolution
- File attached looks ok on computer screen but does not print the same
- We are wanting it to print like it looks on the screen
- We are wanting it to print not fuzzy in resolution
- We are wanting the banner to be on the absolute edge of the page like it is on the computer screen
- We are needing to print this to paper and pdf with perfect resolution and colour

Please can someone help us!!

I have provided the logo files in our posession. If better resolutions are required please let us know.

We are also wanting 4 simple page templates to be setup in Landscape and Portrait orientation as well once we are happy with the letterhead that is provided samples have been provided
Updates

Hi all I have the vector files available now along with a Colour profile

Requirements
Must have
• Clear when printed on A4 Paper
Should not have
• Blurry images, Colour must be correct (same as Logo) - Please reference our website if need be ..... vornal.com.au

```html
<!DOCTYPE html>
<html lang="en">
<head>
<meta charset="UTF-8">
<title>Vornal Pavement Services – Letterhead</title>
<link rel="stylesheet" href="https://fonts.googleapis.com/css2?family=Montserrat:wght@800&display=swap">
<style>
  :root {
    --page: #ffffff;
    --brand-green: #0a7a40;
    --brand-navy: #22408f;
    --ink: #2b2d33;
  }
  * { margin: 0; padding: 0; box-sizing: border-box; }
  html, body {
    width: 1200px;
    height: 1000px;
    overflow: hidden;
    background: var(--page);
  }
  .letterhead {
    position: relative;
    width: 1200px;
    height: 1000px;
    background: var(--page);
  }
  .band {
    position: absolute;
    left: 0;
    display: flex;
    align-items: stretch;
    gap: 6px;
  }
  .band-header { top: 27px; height: 30px; }
  .band-footer { top: 893px; height: 33px; }
  .band-bar { background: var(--brand-green); }
  .band-cap { background: var(--brand-navy); width: 52px; }
  .band-header .band-bar { width: 590px; }
  .band-footer .band-bar { width: 820px; }
  .wordmark {
    position: absolute;
    left: 900px;
    top: 884px;
    width: 255px;
    text-align: right;
    font-family: "Montserrat", sans-serif;
    font-weight: 800;
    line-height: 1;
  }
  .wordmark-name {
    display: block;
    font-size: 56px;
    letter-spacing: 1px;
    color: var(--brand-navy);
  }
  .wordmark-tagline {
    display: block;
    margin-top: 8px;
    font-size: 14px;
    letter-spacing: 0.5px;
    color: var(--ink);
  }
</style>
</head>
<body>
  <main class="letterhead">
    <div class="band band-header" aria-hidden="true">
      <span class="band-bar"></span>
      <span class="band-cap"></span>
    </div>

    <div class="band band-footer" aria-hidden="true">
      <span class="band-bar"></span>
      <span class="band-cap"></span>
    </div>

    <div class="wordmark">
      <span class="wordmark-name">VORNAL</span>
      <span class="wordmark-tagline">PAVEMENT SERVICES</span>
    </div>
  </main>
</body>
</html>
```